SilverLedgerOak - Double Sided Business Card

We are looking for design options or our business cards. We are a Business Solutions and HR solutions Provider - the theme is business, for this card.

Our brand colours are represented within our logo.

Details needed to be put on the front of the business card are:

Employees name: [Sample Name]
Role: [Sample Role]

Address: Suite 4 - Level 3/48 Halloran Avenue Parramatta NSW 2150
M: 0000 000 000
P: 1300 847 213
F: 1300 847 286
E: sample@silverledgeroak.com.au
www.silverledgeroak.com.au
Updates

Reason: Hello, could we please increase our deadline by 5 days. Thanking you, Tess

Target Market(s)

Business Owners, also Candidates looking for Employment

Industry/Entity Type

Business

Contact Information for Business Card

Role: [Sample Role]

M: 0000 000 000
P: 1300 847 213
F: 1300 847 286

Font styles to use
Sans Serif

Colors
3276b5
3176b5
0455a3
85abd2
cfdeed
ffffff
000000
1b1b1b
757575

Requirements
Must have
• Details needed to be put on the front of the business card are:
• Employees name: [Sample Name]
• Role: [Sample Role]
• Address: Suite 4 - Level 3/48 Halloran Avenue Parramatta NSW 2150
• M: 0000 000 000
• P: 1300 847 213
• F: 1300 847 286
• E: sample@silverledgeroak.com.au
• www.silverledgeroak.com.au
Nice to have
• Simplicity, clean and professional.

```html
<!DOCTYPE html>
<html lang="en">
<head>
<meta charset="utf-8">
<title>SilverLedgerOak – Business Card</title>
<link href="https://fonts.googleapis.com/css2?family=Open+Sans:wght@400;600;700&display=swap" rel="stylesheet">
<style>
  :root {
    --navy: #0f2746;
    --brand-blue: #0455a3;
    --mid-blue: #3176b5;
    --pale-blue: #cfdeed;
    --white: #ffffff;
    --ink: #1b1b1b;
    --grey: #757575;
    --backdrop: #e6e8eb;
  }
  * { box-sizing: border-box; margin: 0; padding: 0; }
  html, body { width: 1200px; height: 786px; overflow: hidden; }
  body {
    background: var(--backdrop);
    font-family: "Open Sans", Arial, sans-serif;
    display: flex;
    align-items: center;
    justify-content: center;
    gap: 60px;
  }
  .card {
    position: relative;
    width: 525px;
    height: 300px;
    overflow: hidden;
    box-shadow: 0 10px 28px rgba(0,0,0,.18);
  }

  /* Front */
  .card--front { background: var(--white); color: var(--grey); }
  .card__edge { position: absolute; left: 0; bottom: 0; width: 525px; height: 16px; }
  .brand {
    position: absolute; left: 36px; top: 30px;
    display: flex; align-items: center; gap: 8px;
  }
  .brand__square { width: 14px; height: 14px; background: var(--brand-blue); }
  .brand__name { font-weight: 700; font-size: 20px; color: var(--brand-blue); letter-spacing: .5px; }
  .brand__tagline {
    position: absolute; left: 36px; top: 60px;
    font-size: 8.5px; font-weight: 600; color: var(--navy);
    border-top: 1px solid var(--navy); padding-top: 3px;
  }
  .person { position: absolute; left: 36px; top: 92px; }
  .person__name { font-size: 16px; font-weight: 600; color: var(--brand-blue); text-transform: uppercase; }
  .person__role { font-size: 12px; color: var(--grey); }
  .person__rule { width: 14px; height: 2px; background: var(--brand-blue); margin-top: 8px; }
  .contacts { position: absolute; left: 36px; top: 146px; list-style: none; font-size: 11.5px; line-height: 17px; }
  .contacts li { display: flex; align-items: center; gap: 8px; }
  .contacts svg { width: 11px; height: 11px; fill: var(--navy); flex: none; }
  .contacts .web { color: var(--brand-blue); }
  .address { position: absolute; left: 36px; top: 236px; font-size: 11.5px; line-height: 16px; width: 230px; }

  /* Back */
  .card--back {
    background: var(--navy); color: var(--white);
    display: flex; flex-direction: column; align-items: center; justify-content: center;
  }
  .back-brand { display: flex; align-items: center; gap: 10px; }
  .back-brand__square { width: 18px; height: 18px; background: var(--white); }
  .back-brand__name { font-weight: 700; font-size: 28px; letter-spacing: .5px; }
  .back-tagline {
    margin-top: 8px; padding-top: 4px; border-top: 1px solid var(--white);
    font-size: 10px; font-weight: 600;
  }
</style>
</head>
<body>

  <section class="card card--front" aria-label="Card front">
    <svg class="card__edge" viewBox="0 0 525 16" aria-hidden="true">
      <polygon points="0,10 525,10 525,16 0,16" fill="#0f2746"/>
      <polygon points="0,4 200,4 210,10 0,10" fill="#0455a3"/>
    </svg>

    <div class="brand">
      <span class="brand__square"></span>
      <span class="brand__name">SilverLedgerOak</span>
    </div>
    <p class="brand__tagline">Helping small to medium business realise their potential</p>

    <div class="person">
      <p class="person__name">Daniel Hart</p>
      <p class="person__role">Founder</p>
      <div class="person__rule"></div>
    </div>

    <ul class="contacts">
      <li><svg viewBox="0 0 12 12"><path d="M2 1h3l1 3-1.5 1a6 6 0 0 0 2.5 2.5L8 6l3 1v3a1 1 0 0 1-1 1A9 9 0 0 1 1 2a1 1 0 0 1 1-1z"/></svg>0000 000 000</li>
      <li><svg viewBox="0 0 12 12"><path d="M3 0h6v12H3zM4 1v9h4V1z"/></svg>1300 847 213</li>
      <li><svg viewBox="0 0 12 12"><path d="M1 5h10v6H1zM3 1h6v3H3z"/></svg>1300 847 286</li>
      <li><svg viewBox="0 0 12 12"><path d="M0 2h12v8H0zM1 3l5 4 5-4v-.2H1z"/></svg>sample@silverledgeroak.com.au</li>
      <li class="web"><svg viewBox="0 0 12 12"><circle cx="6" cy="6" r="5.5"/></svg>www.silverledgeroak.com.au</li>
    </ul>

    <p class="address">Suite 4 - Level 3/48 Halloran Avenue Parramatta NSW 2150</p>
  </section>

  <section class="card card--back" aria-label="Card back">
    <div class="back-brand">
      <span class="back-brand__square"></span>
      <span class="back-brand__name">SilverLedgerOak</span>
    </div>
    <p class="back-tagline">Helping small to medium business realise their potential</p>
  </section>

</body>
</html>
```